Maple Bug Guard Business Cards

A modern business card with a predominantly white background and a sleek design featuring Maple with complimentary greys or blacks to convey a professional and contemporary look.

Front:
Primarily white background. Limited use of company purple color can be neighbored by greys.
Text: Name, Title, Cell Phone, Office Phone, Website, email address

Back:
Background Continuation: The back of the card maintains the white background for consistency.
Company name “Maple” in company color and font, “Bug Guard” underneath or underneath left justified of “Maple.”
A subtle pattern or texture in shades of grey to add depth behind the company Logo in font.

logo color: hex #6212ab
font: antique olive nord D Regular

```html
<!DOCTYPE html>
<html lang="en">
<head>
<meta charset="utf-8">
<title>Maple Bug Guard Business Cards</title>
<link rel="stylesheet" href="https://fonts.googleapis.com/css2?family=Archivo:wdth,wght@125,900&family=Poppins:wght@400&display=swap">
<style>
  :root {
    --brand: #6212ab;
    --stage: #e4e4e6;
    --card-white: #ffffff;
    --card-grey: #ededed;
    --text-grey: #5a5a5a;
    --rule-grey: #b8b8b8;
  }
  * { margin: 0; padding: 0; box-sizing: border-box; }
  html, body { width: 1200px; height: 1200px; overflow: hidden; }
  body {
    background: var(--stage);
    position: relative;
    font-family: "Poppins", sans-serif;
  }
  .card {
    position: absolute;
    top: 303px;
    height: 594px;
    text-align: center;
  }
  .card--back {
    left: 218px;
    width: 369px;
    background: radial-gradient(circle at 50% 45%, #f3f3f3 0%, var(--card-grey) 70%, #e6e6e6 100%);
  }
  .card--front {
    left: 617px;
    width: 364px;
    background: var(--card-white);
  }
  .wordmark {
    position: absolute;
    left: 0;
    right: 0;
    font-family: "Archivo", sans-serif;
    font-weight: 900;
    font-stretch: 125%;
    color: var(--brand);
    line-height: 1;
  }
  .wordmark__main { display: block; font-size: 54px; letter-spacing: -1px; }
  .wordmark__sub { display: block; font-size: 27px; margin-top: 6px; letter-spacing: 0.5px; }
  .card--back .wordmark { top: 255px; }
  .card--front .wordmark { top: 102px; }

  .person {
    position: absolute;
    top: 306px;
    left: 0;
    right: 0;
  }
  .person__name {
    font-family: "Archivo", sans-serif;
    font-weight: 900;
    font-stretch: 125%;
    font-size: 17px;
    color: var(--brand);
    letter-spacing: 0.5px;
    line-height: 1.1;
  }
  .person__title {
    font-size: 16px;
    color: var(--text-grey);
    line-height: 1.2;
  }
  .divider {
    position: absolute;
    left: 114px;
    width: 136px;
    height: 34px;
  }
  .divider--phone { top: 361px; }
  .divider--web { top: 453px; }
  .contact-lines {
    position: absolute;
    left: 0;
    right: 0;
    font-size: 17px;
    line-height: 22px;
    color: var(--text-grey);
  }
  .contact-lines--phone { top: 403px; letter-spacing: 0.6px; }
  .contact-lines--web { top: 488px; }
</style>
</head>
<body>
  <section class="card card--back" aria-label="Card back">
    <div class="wordmark">
      <span class="wordmark__main">Maple</span>
      <span class="wordmark__sub">Bug Guard</span>
    </div>
  </section>

  <section class="card card--front" aria-label="Card front">
    <div class="wordmark">
      <span class="wordmark__main">Maple</span>
      <span class="wordmark__sub">Bug Guard</span>
    </div>

    <div class="person">
      <p class="person__name">DANIEL HARPER</p>
      <p class="person__title">Managing Director</p>
    </div>

    <svg class="divider divider--phone" viewBox="0 0 136 34" aria-hidden="true">
      <line x1="0" y1="17" x2="48" y2="17" stroke="var(--rule-grey)" stroke-width="1"/>
      <line x1="88" y1="17" x2="136" y2="17" stroke="var(--rule-grey)" stroke-width="1"/>
      <circle cx="68" cy="17" r="17" fill="var(--brand)"/>
      <path d="M62 10.5c1-.6 1.8-.3 2.3.6l1.2 2.2c.4.8.2 1.5-.5 2l-.9.6c.6 1.6 1.9 3 3.5 3.6l.6-.9c.5-.7 1.2-.9 2-.5l2.2 1.2c.9.5 1.1 1.3.6 2.3-.7 1.3-2 2-3.5 1.7-4.4-1-7.8-4.4-8.8-8.8-.3-1.5.3-2.8 1.3-4z" fill="#fff"/>
      <path d="M69.5 10.5a5 5 0 0 1 4 4M69.5 8a7.5 7.5 0 0 1 6.5 6.5" fill="none" stroke="#fff" stroke-width="1.1" stroke-linecap="round"/>
    </svg>
    <div class="contact-lines contact-lines--phone">
      <p>044-987 654 321</p>
      <p>044-987 654 321</p>
    </div>

    <svg class="divider divider--web" viewBox="0 0 136 34" aria-hidden="true">
      <line x1="0" y1="17" x2="48" y2="17" stroke="var(--rule-grey)" stroke-width="1"/>
      <line x1="88" y1="17" x2="136" y2="17" stroke="var(--rule-grey)" stroke-width="1"/>
      <circle cx="68" cy="17" r="17" fill="var(--brand)"/>
      <g fill="none" stroke="#fff" stroke-width="1.2">
        <circle cx="68" cy="17" r="8"/>
        <ellipse cx="68" cy="17" rx="3.5" ry="8"/>
        <line x1="60" y1="17" x2="76" y2="17"/>
        <line x1="68" y1="9" x2="68" y2="25"/>
        <path d="M61.5 12.5h13M61.5 21.5h13"/>
      </g>
    </svg>
    <div class="contact-lines contact-lines--web">
      <p>info@mapleguard.com</p>
      <p>www.mapleguardpro.com</p>
    </div>
  </section>
</body>
</html>
```